Single Page Digital Brochure

We are a Sydney based finance company. We lend money to developers. Please see attached example of what we are looking to have produced. We just need a design which can be posted on LINKEDIN

Target Market(s)

Property Developers who are borrowing money

Industry/Entity Type

Finance

Requirements
Must have
• Australian relevant imagery.

TEXT TO INCLUDE:

New Offering from Ferngate Lending
Nice to have
• Design and colour scheme based around our logo (attached)

Please include the same text as the attachment

Please make the design based loosely on the attachment. But do not copy the attachement
Should not have
• Remove Text: 'Settle in under four days'

```html
<!DOCTYPE html>
<html lang="en">
<head>
<meta charset="utf-8">
<title>New Offering from Ferngate Lending</title>
<link rel="stylesheet" href="https://fonts.googleapis.com/css2?family=Montserrat:wght@400;500;600;700;800&display=swap">
<style>
  :root {
    --page: #ffffff;
    --navy-deep: #0f2a3d;
    --navy-panel: rgba(10, 34, 52, 0.72);
    --sky: #3d6f98;
    --harbour: #1d5560;
    --sand: #8a8068;
    --white: #ffffff;
    --ink: #1b1b1b;
    --brand-green: #2b4d35;
  }
  * { box-sizing: border-box; margin: 0; padding: 0; }
  html, body {
    width: 1200px;
    height: 1200px;
    overflow: hidden;
    background: var(--page);
    font-family: "Montserrat", sans-serif;
  }
  .banner {
    position: absolute;
    left: 93px;
    top: 339px;
    width: 1021px;
    height: 531px;
    background: var(--white);
  }
  .hero {
    position: relative;
    width: 1021px;
    height: 406px;
    overflow: hidden;
  }
  .hero-photo {
    position: absolute;
    inset: 0;
    background:
      linear-gradient(180deg, var(--sky) 0%, #2f5877 28%, #5a6a6a 52%, var(--sand) 64%, var(--harbour) 78%, var(--navy-deep) 100%);
  }
  .hero-tint {
    position: absolute;
    inset: 0;
    background: rgba(15, 42, 61, 0.35);
  }
  .hero-panel {
    position: absolute;
    inset: 0;
  }
  .headline-rule {
    position: absolute;
    left: 78px;
    top: 43px;
    width: 3px;
    height: 326px;
    background: var(--white);
  }
  .headline {
    position: absolute;
    left: 110px;
    top: 44px;
    color: var(--white);
    font-weight: 800;
    font-size: 62px;
    line-height: 66px;
    letter-spacing: 0.5px;
    text-transform: uppercase;
  }
  .deal {
    position: absolute;
    left: 616px;
    top: 66px;
    color: var(--white);
  }
  .deal-title {
    font-weight: 700;
    font-size: 24px;
    line-height: 29px;
    text-transform: uppercase;
    letter-spacing: 0.3px;
  }
  .deal-rule {
    width: 333px;
    height: 1.5px;
    background: var(--white);
    margin: 12px 0 14px;
  }
  .deal-list { list-style: none; }
  .deal-item {
    display: flex;
    align-items: center;
    gap: 11px;
    font-size: 15px;
    font-weight: 500;
    height: 25.5px;
    white-space: nowrap;
  }
  .deal-item svg { width: 14px; height: 14px; flex: none; }
  .deal-item b { font-weight: 700; }
  .footer {
    position: relative;
    height: 125px;
  }
  .contact {
    position: absolute;
    left: 68px;
    top: 30px;
    color: var(--ink);
    font-size: 21px;
    font-weight: 500;
  }
  .contact-row {
    display: flex;
    align-items: center;
    height: 38px;
    white-space: nowrap;
  }
  .contact-row + .contact-row { margin-top: 2px; }
  .contact-icon { width: 26px; height: 26px; margin: 0 12px 0 12px; flex: none; }
  .contact-value { color: var(--brand-green); font-weight: 500; }
  .contact-or { margin-left: 8px; }
  .divider {
    position: absolute;
    left: 635px;
    top: 27px;
    height: 80px;
    border-left: 1.5px dashed var(--brand-green);
  }
  .brand {
    position: absolute;
    left: 636px;
    right: 0;
    top: 0;
    bottom: 0;
    display: flex;
    align-items: center;
    justify-content: center;
    gap: 12px;
  }
  .brand-dot {
    width: 22px;
    height: 22px;
    border-radius: 50%;
    background: var(--brand-green);
  }
  .brand-name {
    color: var(--brand-green);
    font-weight: 700;
    font-size: 24px;
    letter-spacing: 1px;
    text-transform: uppercase;
  }
</style>
</head>
<body>
  <main class="banner">
    <section class="hero">
      <div class="hero-photo" role="img" aria-label="Photograph of Sydney Harbour with the Opera House, the Harbour Bridge and the city skyline"></div>
      <div class="hero-tint"></div>
      <svg class="hero-panel" width="1021" height="406" viewBox="0 0 1021 406" aria-hidden="true">
        <polygon points="429,0 1021,0 1021,406 619,406" fill="var(--navy-panel)"/>
      </svg>
      <div class="headline-rule"></div>
      <h1 class="headline">New<br>Offering<br>From<br>Ferngate<br>Lending</h1>
      <div class="deal">
        <h2 class="deal-title">We did<br>just last week</h2>
        <div class="deal-rule"></div>
        <ul class="deal-list">
          <li class="deal-item"><svg viewBox="0 0 14 14"><circle cx="7" cy="7" r="6" fill="none" stroke="#fff" stroke-width="1.2"/><path d="M4.3 7.2l1.8 1.8 3.6-3.7" fill="none" stroke="#fff" stroke-width="1.2"/></svg><span><b>Loan Amount:</b> $750,000</span></li>
          <li class="deal-item"><svg viewBox="0 0 14 14"><circle cx="7" cy="7" r="6" fill="none" stroke="#fff" stroke-width="1.2"/><path d="M4.3 7.2l1.8 1.8 3.6-3.7" fill="none" stroke="#fff" stroke-width="1.2"/></svg><span><b>Rate:</b> 7.79%</span></li>
          <li class="deal-item"><svg viewBox="0 0 14 14"><circle cx="7" cy="7" r="6" fill="none" stroke="#fff" stroke-width="1.2"/><path d="M4.3 7.2l1.8 1.8 3.6-3.7" fill="none" stroke="#fff" stroke-width="1.2"/></svg><span><b>Term:</b> 12months</span></li>
          <li class="deal-item"><svg viewBox="0 0 14 14"><circle cx="7" cy="7" r="6" fill="none" stroke="#fff" stroke-width="1.2"/><path d="M4.3 7.2l1.8 1.8 3.6-3.7" fill="none" stroke="#fff" stroke-width="1.2"/></svg><span><b>LVR:</b> 60%</span></li>
          <li class="deal-item"><svg viewBox="0 0 14 14"><circle cx="7" cy="7" r="6" fill="none" stroke="#fff" stroke-width="1.2"/><path d="M4.3 7.2l1.8 1.8 3.6-3.7" fill="none" stroke="#fff" stroke-width="1.2"/></svg><span><b>Repayments:</b> Capitalized</span></li>
          <li class="deal-item"><svg viewBox="0 0 14 14"><circle cx="7" cy="7" r="6" fill="none" stroke="#fff" stroke-width="1.2"/><path d="M4.3 7.2l1.8 1.8 3.6-3.7" fill="none" stroke="#fff" stroke-width="1.2"/></svg><span><b>Security:</b> 2x Sydney Residential Properties</span></li>
          <li class="deal-item"><svg viewBox="0 0 14 14"><circle cx="7" cy="7" r="6" fill="none" stroke="#fff" stroke-width="1.2"/><path d="M4.3 7.2l1.8 1.8 3.6-3.7" fill="none" stroke="#fff" stroke-width="1.2"/></svg><span><b>Purpose:</b> Business Working Capital</span></li>
        </ul>
      </div>
    </section>
    <footer class="footer">
      <div class="contact">
        <p class="contact-row">CALL MARCUS TODAY ON -
          <svg class="contact-icon" viewBox="0 0 26 26" aria-hidden="true"><circle cx="13" cy="13" r="12" fill="none" stroke="var(--brand-green)" stroke-width="1.4"/><path d="M9.2 7.2c-.9.6-1.4 1.6-1.2 2.8.5 3.5 3.8 7.3 7.4 8.5 1.1.4 2.2 0 2.9-.8l.4-.5-2.4-2-1.1.9c-1.6-.7-3-2.3-3.6-3.9l1-1-1.7-2.7z" fill="none" stroke="var(--brand-green)" stroke-width="1.3" stroke-linejoin="round"/></svg>
          <span class="contact-value">0400 118 275</span><span class="contact-or">or</span></p>
        <p class="contact-row">EMAIL -
          <svg class="contact-icon" viewBox="0 0 26 26" aria-hidden="true"><circle cx="13" cy="13" r="12" fill="none" stroke="var(--brand-green)" stroke-width="1.4"/><rect x="7.5" y="9" width="11" height="8" fill="none" stroke="var(--brand-green)" stroke-width="1.2"/><path d="M7.5 9l5.5 4.5L18.5 9M7.5 17l4-3.5M18.5 17l-4-3.5" fill="none" stroke="var(--brand-green)" stroke-width="1.1"/></svg>
          <span class="contact-value">marcus@ferngatelending.com</span></p>
      </div>
      <div class="divider"></div>
      <div class="brand">
        <span class="brand-dot"></span>
        <span class="brand-name">Ferngate Lending</span>
      </div>
    </footer>
  </main>
</body>
</html>
```